Doctor in Veterinary Medecine/ veterinarian

I am a vet and would like a buisness card which is simple yet elegant and professional.
My aim is to help as much animals as I can. My main field of expertise are dogs and cats. I would like the card to reflect a "family doctor" feeling.
It should not be the traditional picture of a paw or a dog but yet it should have a sign of a pet on it. I would like to have my name Lina Haddour as well as my profession D.V.M and my number.

Target Market(s)

Lebanese population who have pets

Industry/Entity Type

Doctor

Contact Information for Business Card

Should contain my profession " D.V.M", my full name "Lina Haddour" and my number "0096171552934"

Requirements
Must have
• A certain picture depicting my profession
Nice to have
• Some sort of picture related to pets and animals
Should not have
• A picture of a paw or a dog. I need something more creative

```html
<!DOCTYPE html>
<html lang="en">
<head>
<meta charset="UTF-8">
<title>Lina Haddour, D.V.M – Business Card</title>
<link href="https://fonts.googleapis.com/css2?family=Montserrat:wght@400;500;700&display=swap" rel="stylesheet">
<style>
  :root {
    --page-bg: #d9dcdc;
    --blue-light: #62c6e8;
    --blue-deep: #1797d0;
    --white: #ffffff;
    --ink-on-blue: #ffffff;
    --icon-blue: #1a9bd3;
  }
  html, body {
    margin: 0;
    width: 1200px;
    height: 900px;
    overflow: hidden;
    background: var(--page-bg);
    font-family: "Montserrat", Arial, sans-serif;
  }
  .canvas {
    position: relative;
    width: 1200px;
    height: 900px;
    display: flex;
    align-items: center;
    justify-content: center;
  }
  .card {
    position: relative;
    width: 1050px;
    height: 600px;
    background: var(--white);
    box-shadow: 0 14px 40px rgba(0,0,0,0.18);
    overflow: hidden;
  }
  .card__field {
    position: absolute;
    left: 0; top: 0;
    width: 1050px;
    height: 508px;
    background: linear-gradient(160deg, var(--blue-light) 0%, var(--blue-deep) 100%);
  }
  .card__pet-art {
    position: absolute;
    left: 150px;
    top: 170px;
    width: 330px;
    height: 338px;
    border-radius: 140px 120px 0 0;
    background: linear-gradient(180deg, rgba(255,255,255,0.95), rgba(255,255,255,0.85));
  }
  .card__tab {
    position: absolute;
    right: 0;
    top: 0;
    width: 44px;
    height: 200px;
    background: var(--white);
    border-bottom-left-radius: 10px;
  }
  .card__icons {
    position: absolute;
    right: 22px;
    top: 22px;
    display: flex;
    flex-direction: column;
    gap: 14px;
  }
  .icon-badge {
    width: 44px;
    height: 44px;
    border-radius: 50%;
    background: var(--icon-blue);
    border: 3px solid var(--white);
    display: flex;
    align-items: center;
    justify-content: center;
  }
  .icon-badge svg { width: 22px; height: 22px; }
  .card__details {
    position: absolute;
    right: 100px;
    top: 30px;
    text-align: right;
    color: var(--ink-on-blue);
  }
  .card__name {
    margin: 0;
    font-size: 30px;
    font-weight: 700;
    letter-spacing: 0.5px;
    text-transform: uppercase;
  }
  .card__title {
    margin: 2px 0 0;
    font-size: 18px;
    font-weight: 400;
    letter-spacing: 2px;
  }
  .card__rule {
    width: 300px;
    height: 1px;
    background: rgba(255,255,255,0.8);
    margin: 12px 0 14px auto;
  }
  .card__phone, .card__email {
    margin: 0;
    font-size: 26px;
    font-weight: 500;
    letter-spacing: 0.5px;
  }
  .card__email { margin-top: 18px; font-size: 24px; }
</style>
</head>
<body>
<div class="canvas">
  <div class="card">
    <div class="card__field"></div>
    <div class="card__pet-art" role="img" aria-label="White silhouette of a dog and a cat sitting side by side"></div>
    <div class="card__tab"></div>
    <div class="card__icons">
      <div class="icon-badge">
        <svg viewBox="0 0 24 24" fill="#fff"><circle cx="12" cy="8" r="4"/><path d="M4 21c0-4.4 3.6-7 8-7s8 2.6 8 7z"/></svg>
      </div>
      <div class="icon-badge">
        <svg viewBox="0 0 24 24" fill="none" stroke="#fff" stroke-width="2"><rect x="7" y="3" width="10" height="18" rx="2"/><line x1="11" y1="18" x2="13" y2="18"/></svg>
      </div>
      <div class="icon-badge">
        <svg viewBox="0 0 24 24" fill="none" stroke="#fff" stroke-width="2"><rect x="3" y="6" width="18" height="12" rx="1"/><path d="M3 6l9 7 9-7"/></svg>
      </div>
    </div>
    <div class="card__details">
      <p class="card__name">Lina Haddour</p>
      <p class="card__title">D.V.M</p>
      <div class="card__rule"></div>
      <p class="card__phone">0096171552934</p>
      <p class="card__email">linahaddour@petmail.com</p>
    </div>
  </div>
</div>
</body>
</html>
```